The Gilded Otter Espresso Nook Coffee Card

would like a coffee card designed for our café. Most cards are so boring and I need to stand out from the crowd (The Gilded Otter ). I require our logo on one side or the business name also a place for people to write their name and mobile number (collecting data base) and on the back the following
customer gets a stamp for the 1st three coffees purchased, on the 3rd one they get a free upsize. another 2 stamps and on the 3rd one (6) gets a free coffee, another 2 stamps and the customer gets another upsize (9th coffee purchased) and on the 10th card they recivie a voucher for a free pizza.
small print | one free pizza for dinner dining (not available for takeaways and must book), Cant be used with any other offers, opts in to hear from the herd if there is a deal on. cant trade for cash or gift

```html
<!DOCTYPE html>
<html lang="en">
<head>
<meta charset="utf-8">
<title>The Gilded Otter Espresso Nook – Coffee Card</title>
<link rel="stylesheet" href="https://fonts.googleapis.com/css2?family=Anton&family=Lato:wght@400;700&display=swap">
<style>
  :root {
    --page: #d9d9d9;
    --card: #ffffff;
    --ink: #111111;
    --band-dark: #232021;
    --band-light: #e6e6e6;
    --mark-tint: #e4e3e4;
    --rule: #555555;
    --text-on-dark: #f2f2f2;
  }
  * { box-sizing: border-box; margin: 0; padding: 0; }
  html, body {
    width: 1200px; height: 782px; overflow: hidden;
    background: var(--page);
    font-family: "Lato", sans-serif;
    color: var(--ink);
  }
  .canvas {
    position: relative; width: 1200px; height: 782px;
    display: flex; align-items: center; justify-content: center; gap: 50px;
  }
  .card {
    position: relative; width: 540px; height: 310px;
    background: var(--card); overflow: hidden;
    box-shadow: 0 2px 6px rgba(0,0,0,.15);
  }
  /* front */
  .card-front__mark {
    position: absolute; left: 140px; top: 30px; width: 330px; height: 250px;
    background: var(--mark-tint); border-radius: 90px 120px 40px 40px;
  }
  .card-front__brand {
    position: absolute; left: 150px; top: 56px; width: 340px;
  }
  .brand-name {
    font-family: "Anton", sans-serif; font-size: 48px; line-height: 1;
    letter-spacing: 1px; text-transform: uppercase; color: var(--ink);
    white-space: nowrap;
  }
  .brand-rule { height: 1px; background: var(--rule); margin-top: 6px; }
  .brand-tagline {
    font-family: "Lato", sans-serif; font-size: 15px; letter-spacing: 1px;
    text-transform: uppercase; margin-top: 4px; padding-left: 70px;
  }
  .card-front__fields { position: absolute; left: 40px; top: 168px; width: 400px; }
  .field { margin-bottom: 14px; }
  .field-label {
    font-family: "Anton", sans-serif; font-size: 22px; line-height: 1;
    text-transform: uppercase;
  }
  .field-line { height: 1px; background: var(--rule); margin-top: 4px; }
  .field:first-child .field-line { width: 360px; }
  /* back */
  .card-back__offer {
    height: 62%; background: var(--band-dark); color: var(--text-on-dark);
    padding: 34px 36px 0; font-size: 13.5px; line-height: 1.35;
  }
  .card-back__terms {
    height: 38%; background: var(--band-light); color: var(--ink);
    padding: 14px 36px 0; font-size: 12px; line-height: 1.35;
  }
</style>
</head>
<body>
<main class="canvas">
  <section class="card card-front" aria-label="Card front">
    <div class="card-front__mark" role="img" aria-label="Faint otter silhouette behind the name"></div>
    <div class="card-front__brand">
      <h1 class="brand-name">The Gilded Otter</h1>
      <div class="brand-rule"></div>
      <p class="brand-tagline">Espresso Nook</p>
    </div>
    <div class="card-front__fields">
      <div class="field"><span class="field-label">Name</span><div class="field-line"></div></div>
      <div class="field"><span class="field-label">Mobile</span><div class="field-line"></div></div>
    </div>
  </section>

  <section class="card card-back" aria-label="Card back">
    <div class="card-back__offer">
      <p>Customer gets a stamp for the 1st three coffees purchased, on the 3rd one they get a free upsize. another 2 stamps and on the 3rd one (6) gets a free coffee, another 2 stamps and the customer gets another upsize (9th coffee purchased) and on the 10th card they recivie a voucher for a free pizza.</p>
    </div>
    <div class="card-back__terms">
      <p>One free pizza for dinner dining (not available for takeaways and must book). Cant be used with any other offers, opts in to hear from the herd if there is a deal on. Cant trade for cash or gift</p>
    </div>
  </section>
</main>
</body>
</html>
```